Verdant Drops Supply Product Labels

Hi, I need to have a label designed for my organic essential oil company You completed TRW Solutions for me and I was very happy with the design. TRW is for preparing plans for business restructures but I am launching a website for my real project which is selling organic essential oils. I am seeking a very simple design and have a clear idea of the look, design and style. Same design but for several sizes (bottles) plus labels for packaging. Check out my Facebook page Verdant Drops Supply

Industry/Entity Type

It Company

Font styles to use
Serif

Requirements
Must have
• Be simple, clean, black and white design. I have logo and examples of designs.

```html
<!DOCTYPE html>
<html lang="en">
<head>
<meta charset="utf-8">
<title>Verdant Drops Supply – Product Labels</title>
<link rel="stylesheet" href="https://fonts.googleapis.com/css2?family=Arimo:wght@400;700&display=swap">
<style>
  :root {
    --page-bg: #e4e5e6;
    --label-bg: #f4f4f4;
    --label-edge: #d9dadb;
    --brand-ink: #5a6670;
    --pure-yellow: #d4c43a;
    --rule-yellow: #c9b22c;
    --peppermint: #2f8c6c;
    --rosehip: #a5607a;
    --eyecream: #72a9c0;
    --white: #ffffff;
    --badge-ink: #2d2d2d;
  }
  * { box-sizing: border-box; margin: 0; padding: 0; }
  html, body {
    width: 1200px;
    height: 673px;
    overflow: hidden;
    background: var(--page-bg);
    font-family: "Arimo", Arial, sans-serif;
  }
  .label-set {
    position: absolute;
    left: 80px;
    top: 196px;
    display: flex;
    gap: 40px;
  }
  .label {
    position: relative;
    width: 320px;
    height: 270px;
    background: linear-gradient(180deg, var(--white) 0%, var(--label-bg) 60%, #e9eaeb 100%);
    border: 1px solid var(--label-edge);
    overflow: hidden;
  }
  .brand-name {
    position: absolute;
    top: 16px;
    left: 0;
    width: 100%;
    text-align: center;
    font-size: 15px;
    font-weight: 400;
    color: var(--brand-ink);
    letter-spacing: 0.2px;
  }
  .product-disc {
    position: absolute;
    left: 100px;
    top: 60px;
    width: 150px;
    height: 150px;
    border-radius: 50%;
    display: flex;
    align-items: center;
    justify-content: center;
    padding-top: 30px;
    text-align: center;
    color: var(--white);
    font-weight: 700;
    font-size: 22px;
    line-height: 1.2;
    white-space: nowrap;
  }
  .purity-badge {
    position: absolute;
    left: 50px;
    top: 40px;
    width: 84px;
    height: 84px;
    border-radius: 50%;
    background: var(--pure-yellow);
    border: 3px solid var(--white);
    display: flex;
    align-items: center;
    justify-content: center;
    text-align: center;
    font-size: 11.5px;
    line-height: 1.2;
    color: var(--badge-ink);
  }
  .accent-rule {
    position: absolute;
    left: 0;
    top: 216px;
    width: 100%;
    height: 4px;
    background: var(--rule-yellow);
  }
  .info-band {
    position: absolute;
    left: 0;
    top: 222px;
    width: 100%;
    height: 38px;
    display: flex;
    flex-direction: column;
    align-items: center;
    justify-content: center;
    gap: 4px;
    color: var(--white);
    font-size: 8px;
    letter-spacing: 0.4px;
  }
  .label--peppermint .product-disc,
  .label--peppermint .info-band { background: var(--peppermint); }
  .label--rosehip .product-disc,
  .label--rosehip .info-band { background: var(--rosehip); }
  .label--eyecream .product-disc,
  .label--eyecream .info-band { background: var(--eyecream); }
</style>
</head>
<body>
  <main class="label-set">
    <section class="label label--peppermint">
      <p class="brand-name">Verdant Drops Supply</p>
      <div class="product-disc">Peppermint<br>Oil</div>
      <div class="purity-badge">100% Pure<br>Essential Oil</div>
      <div class="accent-rule"></div>
      <div class="info-band"><span>100 % ORGANIC</span><span>1fl oz / 30ml</span></div>
    </section>
    <section class="label label--rosehip">
      <p class="brand-name">Verdant Drops Supply</p>
      <div class="product-disc">Rosehip<br>Oil</div>
      <div class="purity-badge">100% Pure<br>Essential Oil</div>
      <div class="accent-rule"></div>
      <div class="info-band"><span>100 % ORGANIC</span><span>1fl oz / 30ml</span></div>
    </section>
    <section class="label label--eyecream">
      <p class="brand-name">Verdant Drops Supply</p>
      <div class="product-disc">Eye cream</div>
      <div class="purity-badge">100% Pure<br>Essential Oil</div>
      <div class="accent-rule"></div>
      <div class="info-band"><span>100 % ORGANIC</span><span>1fl oz / 30ml</span></div>
    </section>
  </main>
</body>
</html>
```